Lumen Harbor Business Card Design Project

We have recently rebranded and would like to design new business cards that incorporate the corporate logo - double sided cards with corporate logo on one side and contact details on the other

Target Market(s)

Sophisticated and high net worth investors and finance industry professionals

Industry/Entity Type

Funds Management

Contact Information for Business Card

The card should prominently feature the company name and logo. Other details will be standard contact details for each staff member - name, address, phone, email, website

Colors
0054AA
0677BA
7BADD7
CADEEF
E8F1F8

Requirements
Must have
• Double-sided design with one side prominently featuring the corporate logo and the other side with all standard contact details

```html
<!DOCTYPE html>
<html lang="en">
<head>
<meta charset="utf-8">
<title>Lumen Harbor – Business Card</title>
<link href="https://fonts.googleapis.com/css2?family=Cormorant+SC:wght@600;700&family=Montserrat:wght@400;500&display=swap" rel="stylesheet">
<style>
  :root {
    --brand-deep: #0054AA;
    --brand-mid: #0677BA;
    --brand-soft: #7BADD7;
    --brand-pale: #CADEEF;
    --brand-mist: #E8F1F8;
    --card-top: #1d5593;
    --card-bottom: #16477e;
    --pattern-light: #22599a;
    --pattern-dark: #123a6a;
    --stage: #2b2e33;
    --ink-light: #ffffff;
  }
  * { margin: 0; padding: 0; box-sizing: border-box; }
  html, body {
    width: 1200px; height: 900px; overflow: hidden;
    background: var(--stage);
  }
  .canvas {
    position: relative; width: 1200px; height: 900px;
    display: flex; justify-content: center; align-items: center; gap: 80px;
  }
  .card {
    position: relative; width: 360px; height: 630px;
    border-radius: 4px; overflow: hidden;
    box-shadow: 0 18px 40px rgba(0,0,0,0.45);
  }
  .card-front { background: linear-gradient(170deg, var(--card-top), var(--card-bottom)); }
  .card-back { background: var(--pattern-dark); }

  /* Front: company name set vertically with plain square marker */
  .brand-vertical {
    position: absolute; top: 30px; right: 30px;
    display: flex; flex-direction: column; align-items: center; gap: 12px;
  }
  .brand-square {
    width: 26px; height: 26px; background: var(--ink-light);
  }
  .brand-vertical-name {
    writing-mode: vertical-rl;
    font-family: "Cormorant SC", serif; font-weight: 600;
    font-size: 28px; letter-spacing: 1px; color: var(--ink-light);
  }
  .front-watermark {
    position: absolute; top: 150px; left: 40px;
    width: 150px; height: 150px; border-radius: 6px;
    background: linear-gradient(150deg, rgba(123,173,215,0.28), rgba(123,173,215,0.08));
  }
  .front-divider {
    position: absolute; top: 318px; left: 0; right: 0;
    height: 1px; background: var(--brand-soft); opacity: 0.7;
  }
  .contact-block {
    position: absolute; top: 350px; left: 40px; right: 30px;
    color: var(--ink-light);
  }
  .person-name {
    font-family: "Cormorant SC", serif; font-weight: 700;
    font-size: 27px; letter-spacing: 0.5px; line-height: 1;
  }
  .person-role {
    font-family: "Montserrat", sans-serif; font-size: 14px;
    margin-top: 4px; color: var(--brand-mist);
  }
  .role-rule {
    width: 100%; height: 1px; background: var(--brand-soft);
    opacity: 0.7; margin: 20px 0 18px;
  }
  .address, .contact-list {
    font-family: "Montserrat", sans-serif; font-size: 15px;
    line-height: 1.45; color: var(--brand-mist);
  }
  .contact-list { list-style: none; margin-top: 10px; }
  .contact-list li { display: flex; align-items: center; gap: 10px; }
  .contact-icon { width: 13px; height: 13px; flex: none; }

  /* Back: tonal pattern field with company name */
  .pattern-field {
    position: absolute; inset: 0;
    background:
      radial-gradient(circle at 30% 20%, rgba(123,173,215,0.22), transparent 55%),
      radial-gradient(circle at 80% 75%, rgba(6,119,186,0.25), transparent 50%),
      linear-gradient(160deg, var(--pattern-light), var(--pattern-dark));
  }
  .brand-horizontal {
    position: absolute; left: 40px; bottom: 120px;
    display: flex; align-items: center; gap: 12px;
  }
  .brand-horizontal-name {
    font-family: "Cormorant SC", serif; font-weight: 600;
    font-size: 30px; letter-spacing: 1px; color: var(--ink-light);
  }
</style>
</head>
<body>
<main class="canvas">
  <section class="card card-front" aria-label="Card front with contact details">
    <div class="brand-vertical">
      <span class="brand-square" aria-hidden="true"></span>
      <span class="brand-vertical-name">Lumen Harbor</span>
    </div>
    <div class="front-watermark" role="img" aria-label="Faint tonal brand watermark"></div>
    <div class="front-divider"></div>
    <div class="contact-block">
      <h1 class="person-name">Dorian Vale</h1>
      <p class="person-role">CEO/Founder</p>
      <div class="role-rule"></div>
      <p class="address">Po Box 4120 Harbor Lane<br>Westmere AB 7310</p>
      <ul class="contact-list">
        <li>
          <svg class="contact-icon" viewBox="0 0 24 24" aria-hidden="true"><path fill="#E8F1F8" d="M6.6 10.8a15.1 15.1 0 0 0 6.6 6.6l2.2-2.2a1 1 0 0 1 1-.25 11.4 11.4 0 0 0 3.6.57 1 1 0 0 1 1 1V20a1 1 0 0 1-1 1A17 17 0 0 1 3 4a1 1 0 0 1 1-1h3.5a1 1 0 0 1 1 1c0 1.25.2 2.450.57 3.6a1 1 0 0 1-.25 1z"/></svg>
          (555) 014-2290
        </li>
        <li>
          <svg class="contact-icon" viewBox="0 0 24 24" aria-hidden="true"><rect x="2" y="5" width="20" height="14" rx="1.5" fill="#E8F1F8"/><path d="M3 6l9 7 9-7" fill="none" stroke="#16477e" stroke-width="1.8"/></svg>
          info@lumenharbor.com
        </li>
        <li>
          <svg class="contact-icon" viewBox="0 0 24 24" aria-hidden="true"><circle cx="12" cy="12" r="10" fill="#E8F1F8"/><path d="M2 12h20M12 2c3 3 3 17 0 20M12 2c-3 3-3 17 0 20" fill="none" stroke="#16477e" stroke-width="1.4"/></svg>
          www.lumenharbor.com
        </li>
      </ul>
    </div>
  </section>

  <section class="card card-back" aria-label="Card back with company name">
    <div class="pattern-field" role="img" aria-label="Tonal embossed repeat pattern in deep blue covering the card"></div>
    <div class="brand-horizontal">
      <span class="brand-square" aria-hidden="true"></span>
      <span class="brand-horizontal-name">Lumen Harbor</span>
    </div>
  </section>
</main>
</body>
</html>
```